Business Card and Letterhead for Pemlo - modern real estate business

I need a double sided business card design for Pemlo. Please see business card brief here https://files.quillnote-hub.net/page/7RtxQmZbn4LsWe2VyHoPk9dFjuC3gaXrTmqEi5Ns_pz/view?mode=shared

Please feel free to design the business cards however you feel best. I am happy to give some creative freedoms and then provide feedback from there.

Please then also create a letterhead to match the business card design

Colors

Designer to choose colors to be used in the design.

Requirements
Must have
• Must be a modern, elegant business card which looks very professional

```html
<!DOCTYPE html>
<html lang="en">
<head>
<meta charset="utf-8">
<title>Pemlo – Business Card</title>
<link href="https://fonts.googleapis.com/css2?family=Montserrat:wght@400;500;600;700&display=swap" rel="stylesheet">
<style>
  :root {
    --bg: #1e1e1e;
    --card-black: #050505;
    --brand-red: #e11b22;
    --text-light: #f2f2f2;
    --photo-dark: #2a2a22;
    --photo-green: #3d4a2c;
    --photo-haze: #4a4c48;
    --font-main: "Montserrat", Arial, sans-serif;
  }
  * { margin: 0; padding: 0; box-sizing: border-box; }
  html, body {
    width: 1200px; height: 900px; overflow: hidden;
    background: var(--bg);
    font-family: var(--font-main);
  }
  .canvas { position: relative; width: 1200px; height: 900px; }

  .card {
    position: absolute; left: 250px;
    width: 700px; height: 400px;
    overflow: hidden;
    box-shadow: 0 10px 30px rgba(0,0,0,.5);
  }

  /* Back side */
  .card-back { top: 35px; background: var(--card-black); }
  .card-back .wordmark {
    position: absolute; left: 0; right: 0; top: 120px;
    text-align: center;
    font-size: 104px; font-weight: 600; letter-spacing: 6px;
    color: var(--brand-red); text-transform: uppercase;
  }
  .card-back .site {
    position: absolute; left: 0; right: 0; bottom: 38px;
    text-align: center; font-size: 16px; letter-spacing: 1.5px;
    color: var(--text-light);
  }
  .card-back .site strong { color: var(--brand-red); font-weight: 700; }

  /* Front side */
  .card-front { top: 465px; background: var(--card-black); }
  .portrait-area {
    position: absolute; inset: 0;
    background:
      radial-gradient(ellipse at 30% 35%, var(--photo-green) 0%, transparent 55%),
      radial-gradient(ellipse at 85% 70%, var(--photo-green) 0%, transparent 50%),
      linear-gradient(180deg, var(--photo-haze) 0%, var(--photo-dark) 60%, #1a1a16 100%);
    opacity: .75;
  }
  .front-wordmark {
    position: absolute; right: 50px; top: 70px;
    font-size: 52px; font-weight: 600; letter-spacing: 3px;
    color: var(--brand-red); text-transform: uppercase;
  }
  .divider {
    position: absolute; left: 60px; right: 50px; top: 255px;
    height: 2px; background: var(--brand-red);
  }
  .name-accent {
    position: absolute; left: 28px; top: 266px;
    width: 7px; height: 38px; background: var(--brand-red);
  }
  .agent {
    position: absolute; left: 50px; top: 264px;
  }
  .agent-name {
    font-size: 28px; font-weight: 600; letter-spacing: 1.5px;
    color: var(--brand-red); text-transform: uppercase; line-height: 1.1;
  }
  .agent-title {
    font-size: 17px; color: var(--text-light); margin-top: 4px; letter-spacing: .5px;
  }
  .address {
    position: absolute; right: 50px; top: 196px;
    text-align: right; font-size: 18px; line-height: 1.3;
    color: var(--text-light); letter-spacing: 1px;
  }
  .contacts {
    position: absolute; right: 30px; top: 276px;
    list-style: none; color: var(--text-light);
    font-size: 18px; letter-spacing: 1px;
  }
  .contacts li {
    display: flex; justify-content: flex-end; align-items: center;
    gap: 14px; height: 32px;
  }
  .contacts svg { width: 16px; height: 16px; flex: none; }
</style>
</head>
<body>
<div class="canvas">

  <section class="card card-back" aria-label="Business card back">
    <div class="wordmark">Pemlo</div>
    <div class="site">www.<strong>pemlo</strong>.com</div>
  </section>

  <section class="card card-front" aria-label="Business card front">
    <div class="portrait-area" role="img" aria-label="Darkened portrait photo of the agent in a dark suit against a blurred bushland view"></div>

    <div class="front-wordmark">Pemlo</div>

    <div class="address">PO Box 1190<br>Ashgrove NSW 2614</div>

    <div class="divider"></div>
    <div class="name-accent"></div>
    <div class="agent">
      <div class="agent-name">Liam Carter</div>
      <div class="agent-title">Licenced Real Estate Agent</div>
    </div>

    <ul class="contacts">
      <li>0400 318 592
        <svg viewBox="0 0 16 16" aria-hidden="true"><path d="M4 1.5l2.2 3-1.4 1.6c.9 2 2.3 3.4 4.2 4.3l1.6-1.4 3 2.2-1.3 2.6C7.5 13.6 2.4 8.5 1.6 3z" fill="#e11b22"/></svg>
      </li>
      <li>liam@pemlo.com
        <svg viewBox="0 0 16 16" aria-hidden="true"><rect x="1.5" y="3.5" width="13" height="9" fill="none" stroke="#e11b22" stroke-width="1.4"/><path d="M1.5 3.5L8 9l6.5-5.5" fill="none" stroke="#e11b22" stroke-width="1.4"/></svg>
      </li>
      <li>www.pemlo.com
        <svg viewBox="0 0 16 16" aria-hidden="true"><g fill="none" stroke="#e11b22" stroke-width="1.2"><circle cx="8" cy="8" r="6.5"/><ellipse cx="8" cy="8" rx="3" ry="6.5"/><path d="M1.5 8h13M2.5 4.8h11M2.5 11.2h11"/></g></svg>
      </li>
    </ul>
  </section>

</div>
</body>
</html>
```